Long term design collaboration - mobile app design & web app design

We are looking for a talented mobile designer to help us improve our UI & UX for mobile app and web app.

The screens that need to be redesigned are attached.

There is potentially a lot more work in future design available for the successful candidate.
The successful candidate would have to take part in daily stand-up around 3 times per week.
The successful candidate would join a dev team
We are software company that does property management

```html
<!DOCTYPE html>
<html lang="en">
<head>
<meta charset="utf-8">
<title>Property Manager – Mobile Screens</title>
<link rel="stylesheet" href="https://fonts.googleapis.com/css2?family=Poppins:wght@400;500;600&display=swap">
<style>
:root{
  --stage:#888888;
  --blue:#2857d3;
  --blue-soft:#eef2fb;
  --ink:#1c1c1e;
  --muted:#7c7c84;
  --card:#ffffff;
  --line:#e6e8ee;
  --shadow:0 2px 10px rgba(30,40,80,.07);
}
*{box-sizing:border-box;margin:0;padding:0}
html,body{width:1200px;height:2858px;overflow:hidden;background:var(--stage)}
body{font-family:'Poppins',sans-serif;color:var(--ink)}
.board{position:absolute;left:0;top:0;width:898px;height:2139px;transform:scale(1.33630);transform-origin:0 0}
.screen{position:absolute;background:#fff;overflow:hidden}
.status{position:absolute;left:0;right:0;top:0;height:48px;display:flex;align-items:center;justify-content:space-between;padding:0 16px 0 32px;font-size:15px;font-weight:500}
.status svg{display:block}
.title-bar{position:absolute;left:0;right:0;display:flex;align-items:center;justify-content:center;font-size:19px;font-weight:500}
.title-bar .back{position:absolute;left:26px;top:50%;transform:translateY(-50%)}
/* dashboard */
.dash{left:49px;top:75px;width:375px;height:1988px;background:var(--blue)}
.dash .status{color:#fff}
.profile{position:absolute;left:27px;top:56px;display:flex;align-items:center;gap:8px;color:#fff;font-size:16px;font-weight:500}
.avatar{width:50px;height:50px;border-radius:50%;background:radial-gradient(circle at 50% 40%,#c9a58c,#5a3a2a 70%);border:2px solid rgba(255,255,255,.4)}
.bell{position:absolute;right:24px;top:68px}
.dash-body{position:absolute;left:0;right:0;top:140px;bottom:0;background:#fff;border-radius:30px 30px 0 0;padding:0 24px 0 27px}
.dash-body .title-bar{top:30px;height:34px;justify-content:flex-start;padding-left:48px}
.dash-body .title-bar .back{left:26px}
.sections{position:absolute;left:27px;right:24px;top:82px}
.group-label{font-size:13px;color:var(--blue);margin:0 0 17px;height:14px;line-height:14px}
.group{margin-bottom:36px}
.row{display:flex;align-items:center;height:70px;border-radius:10px;background:var(--card);box-shadow:var(--shadow);padding:0 16px 0 14px;margin-bottom:11px}
.row.tall{height:83px}
.icon{width:40px;height:40px;border-radius:8px;background:var(--blue-soft);display:flex;align-items:center;justify-content:center;flex:none}
.row-text{flex:1;margin-left:16px}
.row-text h4{font-size:15px;font-weight:500;line-height:20px}
.row-text p{font-size:12px;color:var(--muted);margin-top:3px;line-height:15px}
.chev{flex:none}
.nav{position:absolute;left:0;right:0;bottom:0;height:80px;background:#fff;border-radius:22px 22px 0 0;box-shadow:0 -4px 14px rgba(0,0,0,.05)}
.nav-item{position:absolute;top:18px;width:60px;margin-left:-30px;text-align:center;font-size:10px;color:var(--muted)}
.nav-item svg{display:block;margin:0 auto 4px}
.nav-item.active{color:var(--blue);font-weight:600}
.search-fab{position:absolute;left:50%;top:-28px;width:42px;height:42px;margin-left:-21px;background:var(--blue);border-radius:10px;transform:rotate(45deg);box-shadow:0 4px 10px rgba(40,87,211,.35)}
.search-fab svg{position:absolute;left:9px;top:9px;transform:rotate(-45deg)}
.home-bar{position:absolute;left:50%;bottom:8px;width:128px;height:3px;margin-left:-64px;border-radius:2px;background:#bdbdbd}
/* finances */
.fin{left:474px;top:75px;width:375px;height:825px}
.fin .title-bar{top:64px;height:28px}
.section-title{position:absolute;left:27px;font-size:18px;font-weight:600;color:var(--blue)}
.stat-card{position:absolute;left:27px;width:324px;background:#fff;border-radius:10px;box-shadow:var(--shadow);padding:12px 14px}
.stat-card h5{font-size:15px;font-weight:500}
.stats{display:flex;margin-top:14px}
.stat{width:110px}
.stat .icon{margin-bottom:9px}
.stat small{display:block;font-size:12px;color:var(--muted)}
.stat strong{display:block;font-size:16px;font-weight:600;margin-top:4px}
.stat-card .chev{position:absolute;right:16px;top:50%;margin-top:-8px}
/* legionellas */
.leg{left:474px;top:979px;width:375px;height:811px}
.leg .title-bar{top:66px;height:28px}
.question{top:125px}
.option{position:absolute;left:27px;width:324px;background:#fff;border-radius:10px;box-shadow:var(--shadow);display:flex;align-items:center;padding:0 14px;font-size:15px;line-height:24px}
.radio{width:17px;height:17px;border:1.5px solid #444;border-radius:50%;flex:none;margin-right:12px}
.btn{position:absolute;top:701px;height:41px;width:156px;border-radius:4px;font-size:12px;font-weight:600;letter-spacing:1.5px;display:flex;align-items:center;justify-content:center}
.btn.ghost{left:27px;border:1px solid var(--blue);color:var(--blue);background:#fff}
.btn.solid{left:195px;background:var(--blue);color:#fff}
</style>
</head>
<body>
<div class="board">

  <!-- Development overview -->
  <section class="screen dash">
    <div class="status"><span>9:09</span>
      <svg width="68" height="12" viewBox="0 0 68 12" fill="#fff"><rect x="0" y="8" width="3" height="4"/><rect x="5" y="6" width="3" height="6"/><rect x="10" y="3" width="3" height="9"/><rect x="15" y="0" width="3" height="12"/><path d="M26 4a10 10 0 0 1 14 0l-1.5 1.5a8 8 0 0 0-11 0zM29 7a6 6 0 0 1 8 0l-4 4z"/><rect x="44" y="1" width="22" height="10" rx="3" fill="none" stroke="#fff"/><rect x="46" y="3" width="18" height="6" rx="1.5"/></svg>
    </div>
    <div class="profile"><div class="avatar" role="img" aria-label="Profile photo of the signed-in user"></div>Laura Bennett</div>
    <svg class="bell" width="26" height="28" viewBox="0 0 26 28"><path d="M5 20V12a7 7 0 0 1 14 0v8l2 2H3z" fill="#fff"/><circle cx="12" cy="25" r="2.5" fill="#fff"/><circle cx="19" cy="7" r="6" fill="#e8424b"/><text x="19" y="10" font-size="8" fill="#fff" text-anchor="middle" font-family="Poppins,sans-serif">3</text></svg>

    <div class="dash-body">
      <div class="title-bar">
        <svg class="back" width="10" height="18" viewBox="0 0 10 18"><path d="M8 2 2 9l6 7" fill="none" stroke="#1c1c1e" stroke-width="2" stroke-linecap="round"/></svg>
        Development Overview
      </div>
      <div class="sections">
        <div class="group">
          <div class="group-label">General</div>
          <div class="row"><div class="icon"><svg width="20" height="20" viewBox="0 0 20 20" fill="none" stroke="#2857d3" stroke-width="1.4"><rect x="2" y="4" width="16" height="14" rx="3"/><path d="M2 8h16M6 2v4M14 2v4M6 12h1M10 12h1M14 12h1M6 15h1M10 15h1"/></svg></div><div class="row-text"><h4>Handover date</h4><p>12 January 2023</p></div><svg class="chev" width="8" height="14" viewBox="0 0 8 14"><path d="M1 1l6 6-6 6" fill="none" stroke="#1c1c1e" stroke-width="1.5"/></svg></div>
          <div class="row"><div class="icon"><svg width="20" height="20" viewBox="0 0 20 20" fill="none" stroke="#2857d3" stroke-width="1.4"><path d="M10 2l7 4v8l-7 4-7-4V6zM3 6l7 4 7-4M10 10v8M6.5 4l7 4"/></svg></div><div class="row-text"><h4>Units</h4><p>85</p></div><svg class="chev" width="8" height="14" viewBox="0 0 8 14"><path d="M1 1l6 6-6 6" fill="none" stroke="#1c1c1e" stroke-width="1.5"/></svg></div>
          <div class="row tall"><div class="icon"><svg width="20" height="20" viewBox="0 0 20 20" fill="none" stroke="#2857d3" stroke-width="1.4"><path d="M10 18s6-5.5 6-10a6 6 0 0 0-12 0c0 4.5 6 10 6 10z"/><circle cx="10" cy="8" r="2.3"/></svg></div><div class="row-text"><h4>Address</h4><p>24 Marlow Crescent, London,<br>N4 2QT</p></div><svg class="chev" width="8" height="14" viewBox="0 0 8 14"><path d="M1 1l6 6-6 6" fill="none" stroke="#1c1c1e" stroke-width="1.5"/></svg></div>
          <div class="row"><div class="icon"><svg width="20" height="20" viewBox="0 0 20 20" fill="none" stroke="#2857d3" stroke-width="1.4"><rect x="2" y="2" width="16" height="16" rx="4"/><rect x="5" y="5" width="10" height="10" rx="2"/><path d="M7 8h2v4H7M13 8h-2l2 2-2 2h2"/></svg></div><div class="row-text"><h4>Section 20 limit</h4><p>£20</p></div><svg class="chev" width="8" height="14" viewBox="0 0 8 14"><path d="M1 1l6 6-6 6" fill="none" stroke="#1c1c1e" stroke-width="1.5"/></svg></div>
        </div>

        <div class="group">
          <div class="group-label">Compliance</div>
          <div class="row"><div class="icon"><svg width="20" height="20" viewBox="0 0 20 20" fill="none" stroke="#2857d3" stroke-width="1.4"><rect x="3" y="2" width="14" height="16" rx="3"/><path d="M7 11h6M7 14h4"/></svg></div><div class="row-text"><h4>Asbestos</h4><p>NA</p></div><svg class="chev" width="8" height="14" viewBox="0 0 8 14"><path d="M1 1l6 6-6 6" fill="none" stroke="#1c1c1e" stroke-width="1.5"/></svg></div>
          <div class="row"><div class="icon"><svg width="20" height="20" viewBox="0 0 20 20" fill="none" stroke="#2857d3" stroke-width="1.4"><rect x="3" y="4" width="14" height="14" rx="3"/><path d="M7 2v4M13 2v4M7 11h6M7 14h4"/></svg></div><div class="row-text"><h4>EICR</h4><p>85</p></div><svg class="chev" width="8" height="14" viewBox="0 0 8 14"><path d="M1 1l6 6-6 6" fill="none" stroke="#1c1c1e" stroke-width="1.5"/></svg></div>
          <div class="row"><div class="icon"><svg width="20" height="20" viewBox="0 0 20 20" fill="none" stroke="#2857d3" stroke-width="1.4"><rect x="2" y="2" width="16" height="16" rx="3"/><path d="M5 5l3 3M8 5l-3 3M9 14l2 2 4-5M11 6h4"/></svg></div><div class="row-text"><h4>Drains</h4><p>Overdue 10 December 2023</p></div><svg class="chev" width="8" height="14" viewBox="0 0 8 14"><path d="M1 1l6 6-6 6" fill="none" stroke="#1c1c1e" stroke-width="1.5"/></svg></div>
          <div class="row"><div class="icon"><svg width="20" height="20" viewBox="0 0 20 20" fill="none" stroke="#2857d3" stroke-width="1.4"><path d="M4 5h13l-2 13H2z"/><path d="M7 3v4M13 3v4M6 11h7M5 14h5"/></svg></div><div class="row-text"><h4>Gutters</h4><p>NA</p></div><svg class="chev" width="8" height="14" viewBox="0 0 8 14"><path d="M1 1l6 6-6 6" fill="none" stroke="#1c1c1e" stroke-width="1.5"/></svg></div>
          <div class="row"><div class="icon"><svg width="20" height="20" viewBox="0 0 20 20" fill="none" stroke="#2857d3" stroke-width="1.4"><path d="M10 18H5a3 3 0 0 1-3-3V7a3 3 0 0 1 3-3h10a3 3 0 0 1 3 3v3M2 8h16M6 2v4M14 2v4"/><circle cx="15" cy="15" r="3"/><path d="M15 13.5v3M13.5 15h3"/></svg></div><div class="row-text"><h4>Dry Risers</h4><p>NA</p></div><svg class="chev" width="8" height="14" viewBox="0 0 8 14"><path d="M1 1l6 6-6 6" fill="none" stroke="#1c1c1e" stroke-width="1.5"/></svg></div>
        </div>

        <div class="group">
          <div class="group-label">Insurances</div>
          <div class="row"><div class="icon"><svg width="20" height="20" viewBox="0 0 20 20" fill="none" stroke="#2857d3" stroke-width="1.4"><path d="M10 3l8 14H2z" stroke-linejoin="round"/><path d="M10 8v4M10 14.5v.5"/></svg></div><div class="row-text"><h4>Terrorism</h4><p>NA</p></div><svg class="chev" width="8" height="14" viewBox="0 0 8 14"><path d="M1 1l6 6-6 6" fill="none" stroke="#1c1c1e" stroke-width="1.5"/></svg></div>
          <div class="row"><div class="icon"><svg width="20" height="20" viewBox="0 0 20 20" fill="none" stroke="#2857d3" stroke-width="1.4"><path d="M2 18h16M3 18V3h8v15M6 6h2M6 9h2M6 12h2"/><circle cx="15" cy="11" r="2"/><path d="M15 13v5"/></svg></div><div class="row-text"><h4>Buildings</h4><p>NA</p></div><svg class="chev" width="8" height="14" viewBox="0 0 8 14"><path d="M1 1l6 6-6 6" fill="none" stroke="#1c1c1e" stroke-width="1.5"/></svg></div>
          <div class="row"><div class="icon"><svg width="20" height="20" viewBox="0 0 20 20" fill="none" stroke="#2857d3" stroke-width="1.4"><circle cx="10" cy="10" r="2.5"/><path d="M10 2l2 2.5 3-.5.5 3L18 9l-1.5 2.5L17 15l-3 .3L12 18l-2-1.5L8 18l-2-2.7-3-.3.5-3.5L2 9l2.5-2L5 4l3 .5z"/></svg></div><div class="row-text"><h4>Engineering</h4><p>NA</p></div><svg class="chev" width="8" height="14" viewBox="0 0 8 14"><path d="M1 1l6 6-6 6" fill="none" stroke="#1c1c1e" stroke-width="1.5"/></svg></div>
          <div class="row"><div class="icon"><svg width="20" height="20" viewBox="0 0 20 20" fill="none" stroke="#2857d3" stroke-width="1.4"><circle cx="9" cy="6" r="4"/><path d="M2 18c0-3.5 3-6 7-6M12 17l5-5 1.5 1.5-5 5H12z"/></svg></div><div class="row-text"><h4>D &amp; O</h4><p>NA</p></div><svg class="chev" width="8" height="14" viewBox="0 0 8 14"><path d="M1 1l6 6-6 6" fill="none" stroke="#1c1c1e" stroke-width="1.5"/></svg></div>
          <div class="row"><div class="icon"><svg width="20" height="20" viewBox="0 0 20 20" fill="none" stroke="#2857d3" stroke-width="1.4"><circle cx="10" cy="6" r="4"/><path d="M3 18c0-4 3-6 7-6s7 2 7 6z"/></svg></div><div class="row-text"><h4>Reinstatemen</h4><p>NA</p></div><svg class="chev" width="8" height="14" viewBox="0 0 8 14"><path d="M1 1l6 6-6 6" fill="none" stroke="#1c1c1e" stroke-width="1.5"/></svg></div>
        </div>

        <div class="group">
          <div class="group-label">Service Charge</div>
          <div class="row"><div class="icon"><svg width="20" height="20" viewBox="0 0 20 20" fill="none" stroke="#2857d3" stroke-width="1.4"><rect x="2" y="4" width="16" height="14" rx="3"/><path d="M2 8h16M6 2v4M14 2v4M6 12h1M10 12h1M14 12h1M6 15h1M10 15h1"/></svg></div><div class="row-text"><h4>Year End</h4><p>12/12/2024</p></div></div>
          <div class="row"><div class="icon"><svg width="20" height="20" viewBox="0 0 20 20" fill="none" stroke="#2857d3" stroke-width="1.4"><path d="M10 18H5a3 3 0 0 1-3-3V7a3 3 0 0 1 3-3h10a3 3 0 0 1 3 3v3M2 8h16M6 2v4M14 2v4M6 12h1M6 15h1"/><circle cx="15" cy="15" r="3"/><path d="M14 15l1 1 1.5-2"/></svg></div><div class="row-text"><h4>Demand Dates</h4><p>NA</p></div></div>
        </div>

        <div class="group">
          <div class="group-label">Cosec</div>
          <div class="row"><div class="icon"><svg width="20" height="20" viewBox="0 0 20 20" fill="none" stroke="#2857d3" stroke-width="1.4"><circle cx="10" cy="10" r="8"/><path d="M6.5 10l2.5 2.5 4.5-5"/></svg></div><div class="row-text"><h4>Are we responsible?</h4><p>No</p></div></div>
        </div>
      </div>

      <nav class="nav">
        <div class="search-fab"><svg width="24" height="24" viewBox="0 0 24 24" fill="none" stroke="#fff" stroke-width="1.8"><circle cx="11" cy="11" r="7"/><path d="M16 16l4 4"/></svg></div>
        <div class="nav-item active" style="left:52px"><svg width="18" height="18" viewBox="0 0 18 18"><path d="M9 1l8 6v10H1V7z" fill="#2857d3"/><circle cx="9" cy="11" r="2" fill="#fff"/></svg>Home</div>
        <div class="nav-item" style="left:116px"><svg width="18" height="18" viewBox="0 0 18 18" fill="none" stroke="#7c7c84" stroke-width="1.2"><rect x="2" y="1" width="14" height="16" rx="2"/><path d="M5 6h3M10 6h3M5 10h3M10 10h3M5 14h3M10 14h3"/></svg>Overview</div>
        <div class="nav-item" style="left:259px"><svg width="18" height="18" viewBox="0 0 18 18" fill="none" stroke="#7c7c84" stroke-width="1.2"><path d="M3 10V5a3 3 0 0 1 3-3h7a3 3 0 0 1 3 3v5M3 8h13"/><circle cx="5" cy="14" r="3"/><path d="M12 13h3M12 16h3"/></svg>Finances</div>
        <div class="nav-item" style="left:323px"><svg width="18" height="18" viewBox="0 0 18 18" fill="none" stroke="#7c7c84" stroke-width="1.2"><path d="M2 4a2 2 0 0 1 2-2h10a2 2 0 0 1 2 2v8a2 2 0 0 1-2 2H8l-4 3v-3a2 2 0 0 1-2-2z"/><path d="M6 7h6M6 10h4"/></svg>Message</div>
        <div class="home-bar"></div>
      </nav>
    </div>
  </section>

  <!-- Finances -->
  <section class="screen fin">
    <div class="status"><span>9:09</span>
      <svg width="68" height="12" viewBox="0 0 68 12" fill="#1c1c1e"><rect x="0" y="8" width="3" height="4"/><rect x="5" y="6" width="3" height="6"/><rect x="10" y="3" width="3" height="9"/><rect x="15" y="0" width="3" height="12"/><path d="M26 4a10 10 0 0 1 14 0l-1.5 1.5a8 8 0 0 0-11 0zM29 7a6 6 0 0 1 8 0l-4 4z"/><rect x="44" y="1" width="22" height="10" rx="3" fill="none" stroke="#1c1c1e"/><rect x="46" y="3" width="18" height="6" rx="1.5"/></svg>
    </div>
    <div class="title-bar"><svg class="back" width="10" height="18" viewBox="0 0 10 18"><path d="M8 2 2 9l6 7" fill="none" stroke="#1c1c1e" stroke-width="2" stroke-linecap="round"/></svg>Finances</div>

    <h3 class="section-title" style="top:124px">Accounts Receivable</h3>
    <div class="stat-card" style="top:162px;height:151px">
      <h5>Arrears</h5>
      <div class="stats">
        <div class="stat"><div class="icon"><svg width="20" height="20" viewBox="0 0 20 20" fill="none" stroke="#2857d3" stroke-width="1.4"><path d="M3 11V6a3 3 0 0 1 3-3h8a3 3 0 0 1 3 3v5M3 8h14"/><circle cx="5.5" cy="15" r="3"/><path d="M12 13h5M12 16h5"/></svg></div><small>Total</small><strong>£7,268.22</strong></div>
        <div class="stat"><div class="icon"><svg width="20" height="20" viewBox="0 0 20 20" fill="none" stroke="#2857d3" stroke-width="1.4"><rect x="3" y="2" width="14" height="16" rx="3"/><path d="M7 10h6M7 13h4"/></svg></div><small>Bills</small><strong>5</strong></div>
      </div>
      <svg class="chev" width="8" height="14" viewBox="0 0 8 14"><path d="M1 1l6 6-6 6" fill="none" stroke="#1c1c1e" stroke-width="1.5"/></svg>
    </div>
    <div class="stat-card" style="top:324px;height:151px">
      <h5>Unallocated Receipts</h5>
      <div class="stats">
        <div class="stat"><div class="icon"><svg width="20" height="20" viewBox="0 0 20 20" fill="none" stroke="#2857d3" stroke-width="1.4"><path d="M3 11V6a3 3 0 0 1 3-3h8a3 3 0 0 1 3 3v5M3 8h14"/><circle cx="5.5" cy="15" r="3"/><path d="M12 13h5M12 16h5"/></svg></div><small>Total</small><strong>£7,268.22</strong></div>
        <div class="stat"><div class="icon"><svg width="20" height="20" viewBox="0 0 20 20" fill="none" stroke="#2857d3" stroke-width="1.4"><rect x="3" y="2" width="14" height="16" rx="3"/><path d="M7 10h6M7 13h4"/></svg></div><small>Receipts</small><strong>5</strong></div>
      </div>
      <svg class="chev" width="8" height="14" viewBox="0 0 8 14"><path d="M1 1l6 6-6 6" fill="none" stroke="#1c1c1e" stroke-width="1.5"/></svg>
    </div>

    <h3 class="section-title" style="top:506px">Accounts Payable</h3>
    <div class="stat-card" style="top:543px;height:151px">
      <h5>Invoices</h5>
      <div class="stats">
        <div class="stat" style="width:113px"><div class="icon"><svg width="20" height="20" viewBox="0 0 20 20" fill="none" stroke="#2857d3" stroke-width="1.4"><path d="M13 3H5a2 2 0 0 0-2 2v13l2-1.5L7 18l2-1.5L11 18V5a2 2 0 0 1 2-2 2 2 0 0 1 2 2v3h-4M6 8h2M6 11h2"/></svg></div><small>Total</small><strong>£4,268.78</strong></div>
        <div class="stat"><div class="icon"><svg width="20" height="20" viewBox="0 0 20 20" fill="none" stroke="#2857d3" stroke-width="1.4"><rect x="3" y="2" width="14" height="16" rx="3"/><path d="M7 10h6M7 13h4"/></svg></div><small>Invoices</small><strong>5</strong></div>
      </div>
      <svg class="chev" width="8" height="14" viewBox="0 0 8 14"><path d="M1 1l6 6-6 6" fill="none" stroke="#1c1c1e" stroke-width="1.5"/></svg>
    </div>

    <nav class="nav">
      <div class="search-fab"><svg width="24" height="24" viewBox="0 0 24 24" fill="none" stroke="#fff" stroke-width="1.8"><circle cx="11" cy="11" r="7"/><path d="M16 16l4 4"/></svg></div>
      <div class="nav-item active" style="left:52px"><svg width="18" height="18" viewBox="0 0 18 18"><path d="M9 1l8 6v10H1V7z" fill="#2857d3"/><circle cx="9" cy="11" r="2" fill="#fff"/></svg>Home</div>
      <div class="nav-item" style="left:116px"><svg width="18" height="18" viewBox="0 0 18 18" fill="none" stroke="#7c7c84" stroke-width="1.2"><rect x="2" y="1" width="14" height="16" rx="2"/><path d="M5 6h3M10 6h3M5 10h3M10 10h3M5 14h3M10 14h3"/></svg>Overview</div>
      <div class="nav-item" style="left:259px"><svg width="18" height="18" viewBox="0 0 18 18" fill="none" stroke="#7c7c84" stroke-width="1.2"><path d="M3 10V5a3 3 0 0 1 3-3h7a3 3 0 0 1 3 3v5M3 8h13"/><circle cx="5" cy="14" r="3"/><path d="M12 13h3M12 16h3"/></svg>Finances</div>
      <div class="nav-item" style="left:323px"><svg width="18" height="18" viewBox="0 0 18 18" fill="none" stroke="#7c7c84" stroke-width="1.2"><path d="M2 4a2 2 0 0 1 2-2h10a2 2 0 0 1 2 2v8a2 2 0 0 1-2 2H8l-4 3v-3a2 2 0 0 1-2-2z"/><path d="M6 7h6M6 10h4"/></svg>Message</div>
      <div class="home-bar"></div>
    </nav>
  </section>

  <!-- Legionellas -->
  <section class="screen leg">
    <div class="status"><span>9:09</span>
      <svg width="68" height="12" viewBox="0 0 68 12" fill="#1c1c1e"><rect x="0" y="8" width="3" height="4"/><rect x="5" y="6" width="3" height="6"/><rect x="10" y="3" width="3" height="9"/><rect x="15" y="0" width="3" height="12"/><path d="M26 4a10 10 0 0 1 14 0l-1.5 1.5a8 8 0 0 0-11 0zM29 7a6 6 0 0 1 8 0l-4 4z"/><rect x="44" y="1" width="22" height="10" rx="3" fill="none" stroke="#1c1c1e"/><rect x="46" y="3" width="18" height="6" rx="1.5"/></svg>
    </div>
    <div class="title-bar"><svg class="back" width="10" height="18" viewBox="0 0 10 18"><path d="M8 2 2 9l6 7" fill="none" stroke="#1c1c1e" stroke-width="2" stroke-linecap="round"/></svg>Legionellas</div>
    <h3 class="section-title question">Is it required?</h3>
    <div class="option" style="top:167px;height:52px"><span class="radio"></span>No</div>
    <div class="option" style="top:229px;height:76px"><span class="radio"></span>Yes, but I do not have a file to upload</div>
    <div class="option" style="top:315px;height:52px"><span class="radio"></span>Yes, and I have a file to upload</div>
    <div class="btn ghost">BACK</div>
    <div class="btn solid">NEXT ›</div>
  </section>

</div>
</body>
</html>
```